Corporate Design für Veranstalter von Fundraising-Events zum Thema Naturschutz
Zielgruppe
Wir sind eine Organisation, die Fundraising Events zum Thema Naturschutz organisiert. Spenden gehen an internationale Naturschutzprojekte. Unsere Zielgruppe sind große Firmen, wie auch private Spender von jung bis alt.
Aufgabenstellung
Wir suchen ein hochwertiges Design, das auf internationaler Bühne Zuspruch findet. Unternehmenssprache ist Englisch, daher bitte jeglichen Text in englischer Sprache verfassen. Der Name unser Organisation ist Colina Brava, was grüner Schmetterling in Spanisch bedeutet. Unser Logo sollte daher einen grünen Schmetterling enthalten und die Farbe Grün (hellgrün-saftig) die dominante Farbe im Corporate Design sein. Je nach Design könnten wir uns als weitere Farbakzente erdige Töne vorstellen, vorrangig orange.

```html
<!DOCTYPE html>
<html lang="en">
<head>
<meta charset="utf-8">
<title>Colina Brava – Business Card</title>
<link rel="stylesheet" href="https://fonts.googleapis.com/css2?family=Source+Sans+3:wght@400;600&display=swap">
<style>
  :root {
    --backdrop: #f3f1ed;
    --card-white: #ffffff;
    --brand-orange: #ff700c;
    --leaf-green: #3fe046;
    --forest-green: #2a8419;
    --text-on-orange: #ffffff;
  }
  html, body {
    margin: 0;
    padding: 0;
    width: 1113px;
    height: 1200px;
    overflow: hidden;
    background: var(--backdrop);
    font-family: "Source Sans 3", "Myriad Pro", Arial, sans-serif;
  }
  .canvas {
    position: relative;
    width: 1113px;
    height: 1200px;
  }
  .card {
    position: absolute;
    background: var(--card-white);
    overflow: hidden;
  }
  .card-front { left: 226px; top: 159px; width: 690px; height: 389px; }
  .card-back  { left: 228px; top: 597px; width: 688px; height: 388px; }
  .card-shapes {
    position: absolute;
    inset: 0;
    display: block;
  }
  .contact {
    position: absolute;
    left: 333px;
    top: 62px;
    margin: 0;
    color: var(--text-on-orange);
    font-size: 18.5px;
    line-height: 25px;
    font-style: normal;
  }
  .contact p { margin: 0 0 25px; }
  .contact p:last-child { margin-bottom: 0; }
  .brand {
    position: absolute;
    left: 0;
    right: 0;
    top: 180px;
    display: flex;
    align-items: center;
    justify-content: center;
    gap: 16px;
  }
  .brand-dot {
    width: 40px;
    height: 40px;
    border-radius: 50%;
    background: var(--leaf-green);
  }
  .brand-name {
    margin: 0;
    color: var(--forest-green);
    font-size: 46px;
    font-weight: 400;
    letter-spacing: 0.5px;
  }
</style>
</head>
<body>
<main class="canvas">

  <section class="card card-front" aria-label="Business card front">
    <svg class="card-shapes" viewBox="0 0 690 389" aria-hidden="true">
      <polygon fill="var(--forest-green)" points="180,0 222,0 272,192 202,389 155,389 252,196"/>
      <polygon fill="var(--leaf-green)" points="114,0 186,0 272,194 144,389 242,192"/>
      <polygon fill="var(--brand-orange)" points="219,0 690,0 690,389 202,389 272,192"/>
    </svg>
    <address class="contact">
      <p>Colina Brava</p>
      <p>Lindenhofweg 7<br>10437 Berlin</p>
      <p>Tel.:&nbsp; 030/555018240<br>Fax.: 030/ 555018241</p>
      <p>Email: hello@colinabrava-beispiel.de<br>Web:&nbsp;&nbsp; www.colinabrava-beispiel.de</p>
    </address>
  </section>

  <section class="card card-back" aria-label="Business card back">
    <svg class="card-shapes" viewBox="0 0 688 388" aria-hidden="true">
      <polygon fill="var(--brand-orange)" points="0,60 170,66 0,118"/>
      <polygon fill="var(--forest-green)" points="0,0 684,0 0,86"/>
      <polygon fill="var(--brand-orange)" points="402,346 688,253 688,318"/>
      <polygon fill="var(--leaf-green)" points="440,340 688,262 688,318"/>
      <polygon fill="var(--forest-green)" points="8,388 688,316 688,388"/>
    </svg>
    <div class="brand">
      <span class="brand-dot" aria-hidden="true"></span>
      <p class="brand-name">Colina Brava</p>
    </div>
  </section>

</main>
</body>
</html>
```